Velmor Glazing

Modern glazing company specializing in commercial fit outs, pool fencing, frameless showers and glass splash backs, im after a very young/modern logo, it doesnt have to be revelent to glazing and a classy "boss like" design for the card. thank you in advanced

im thinking carbon fiber back ground or something along that line with bright orange wording or something maybe, open to suggestions 

Fencing

company name, name, phone and products

```html
<!DOCTYPE html>
<html lang="en">
<head>
<meta charset="utf-8">
<title>Velmor Glazing – Business Card</title>
<link rel="stylesheet" href="https://fonts.googleapis.com/css2?family=Lato:wght@700;900&display=swap">
<style>
  :root {
    --charcoal: #2e2c2d;
    --orange: #f05a24;
    --white: #ffffff;
    --white-faint: rgba(255, 255, 255, 0.09);
    --backdrop: #e9e6e3;
  }
  * { margin: 0; padding: 0; box-sizing: border-box; }
  html, body {
    width: 1200px;
    height: 1000px;
    overflow: hidden;
    background: var(--backdrop);
    font-family: "Lato", sans-serif;
  }
  .canvas { position: relative; width: 1200px; height: 1000px; }
  .card {
    position: absolute;
    width: 640px;
    height: 380px;
    overflow: hidden;
    box-shadow: 0 10px 26px rgba(0, 0, 0, 0.22);
  }
  .card--back { left: 90px; top: 90px; background: var(--charcoal); }
  .card--front { left: 470px; top: 530px; background: var(--orange); }

  .edge-tab { position: absolute; width: 44px; }
  .card--back .edge-tab { background: var(--orange); }
  .card--front .edge-tab { background: var(--charcoal); }
  .edge-tab--left { left: 0; border-top-right-radius: 40px; }
  .edge-tab--right { right: 0; border-bottom-left-radius: 40px; }
  .card--back .edge-tab--left { top: 150px; bottom: 0; }
  .card--back .edge-tab--right { top: 0; height: 320px; }
  .card--front .edge-tab--left { top: 40px; bottom: 0; }
  .card--front .edge-tab--right { top: 0; height: 345px; border-top-left-radius: 40px; }

  .brand {
    position: absolute;
    left: 0;
    right: 0;
    display: flex;
    align-items: center;
    justify-content: center;
  }
  .brand-mark { flex: none; }
  .brand-name {
    font-weight: 900;
    text-transform: uppercase;
    letter-spacing: 0.02em;
    line-height: 1;
  }
  .card--back .brand { top: 130px; gap: 22px; }
  .card--back .brand-mark { width: 78px; height: 78px; background: var(--orange); }
  .card--back .brand-name { font-size: 46px; color: var(--orange); }
  .card--front .brand { top: 44px; gap: 16px; }
  .card--front .brand-mark { width: 52px; height: 52px; background: var(--white); }
  .card--front .brand-name { font-size: 30px; color: var(--white); }

  .watermark-block {
    position: absolute;
    left: 230px;
    top: 20px;
    width: 240px;
    height: 240px;
    background: var(--white-faint);
  }
  .watermark-name {
    position: absolute;
    left: 0;
    right: 0;
    top: 292px;
    text-align: center;
    font-size: 38px;
    font-weight: 900;
    text-transform: uppercase;
    color: var(--white-faint);
    line-height: 1;
  }

  .holder {
    position: absolute;
    top: 140px;
    left: 0;
    right: 0;
    text-align: center;
    color: var(--white);
  }
  .holder-name { font-size: 28px; font-weight: 900; text-transform: uppercase; line-height: 1.1; }
  .holder-role { font-size: 19px; font-weight: 700; }
  .contact { position: absolute; color: var(--white); font-size: 18px; font-weight: 700; }
  .contact--phone { right: 60px; top: 250px; }
  .contact--email { left: 62px; bottom: 14px; }
</style>
</head>
<body>
<main class="canvas">
  <section class="card card--back" aria-label="Card back">
    <div class="edge-tab edge-tab--left"></div>
    <div class="edge-tab edge-tab--right"></div>
    <div class="brand">
      <span class="brand-mark"></span>
      <p class="brand-name">Velmor Glazing</p>
    </div>
  </section>

  <section class="card card--front" aria-label="Card front">
    <div class="watermark-block" aria-hidden="true"></div>
    <p class="watermark-name" aria-hidden="true">Velmor Glazing</p>
    <div class="edge-tab edge-tab--left"></div>
    <div class="edge-tab edge-tab--right"></div>
    <div class="brand">
      <span class="brand-mark"></span>
      <p class="brand-name">Velmor Glazing</p>
    </div>
    <div class="holder">
      <p class="holder-name">Dean Marlow</p>
      <p class="holder-role">your designation here</p>
    </div>
    <p class="contact contact--phone">Phone : 0412 555 730</p>
    <p class="contact contact--email">Email : Your email id over here.</p>
  </section>
</main>
</body>
</html>
```